IT Company, Needs new Logo and Letterhead Design

We need a Letterhead and possible a new logo for an existing IT Company. We are not happy with our current Letterhead that we are using in our quotes etc. We are happy to change our logo if required. We will upload our current logo and letterhead and look forward to getting some examples. We provide Server, Workstation and network support.

Target Market(s)

Small to Medium Sized Businesses.

Industry/Entity Type

It Company

Requirements
Must have
• Ability to edit the letterhead at a later date. Will need the source files for editing once approved.
Nice to have
• Same colour scheme, but we are open to suggestions.

```html
<!DOCTYPE html>
<html lang="en">
<head>
<meta charset="utf-8">
<title>Voltline Network Solutions – Letterhead</title>
<link href="https://fonts.googleapis.com/css2?family=Open+Sans:ital,wght@0,300;0,400;1,600&display=swap" rel="stylesheet">
<style>
  :root {
    --backdrop: #d9dde3;
    --paper: #ffffff;
    --brand-orange: #f7941d;
    --ink: #2b2b2b;
  }
  * { margin: 0; padding: 0; box-sizing: border-box; }
  html, body {
    width: 1200px;
    height: 1000px;
    overflow: hidden;
    background: var(--backdrop);
    font-family: "Open Sans", Arial, sans-serif;
  }
  .letterhead {
    position: absolute;
    left: 260px;
    top: 20px;
    width: 680px;
    height: 960px;
    background: var(--paper);
    box-shadow: 0 2px 10px rgba(0, 0, 0, 0.12);
  }
  .brand {
    position: absolute;
    left: 44px;
    top: 40px;
    display: flex;
    align-items: center;
    gap: 8px;
  }
  .brand-dot {
    width: 14px;
    height: 14px;
    border-radius: 50%;
    background: var(--brand-orange);
  }
  .brand-name {
    font-weight: 300;
    font-size: 20px;
    line-height: 1.05;
    color: var(--brand-orange);
    letter-spacing: 0.3px;
  }
  .header-rules {
    position: absolute;
    left: 150px;
    right: 40px;
    top: 104px;
  }
  .rule {
    background: var(--brand-orange);
    width: 100%;
  }
  .rule--thick { height: 4px; }
  .rule--thin { height: 1.5px; }
  .header-rules .rule + .rule { margin-top: 7px; }

  .footer {
    position: absolute;
    left: 40px;
    right: 40px;
    bottom: 34px;
  }
  .footer-contact {
    display: flex;
    justify-content: space-between;
    align-items: flex-end;
    font-style: italic;
    font-weight: 600;
    font-size: 10px;
    line-height: 1.35;
    color: var(--ink);
    margin-bottom: 8px;
  }
  .footer-phones { text-align: left; }
  .footer .rule + .rule { margin-top: 6px; }
</style>
</head>
<body>
  <main class="letterhead">
    <header>
      <div class="brand">
        <span class="brand-dot"></span>
        <span class="brand-name">Voltline<br>Network Solutions</span>
      </div>
      <div class="header-rules">
        <div class="rule rule--thick"></div>
        <div class="rule rule--thick"></div>
        <div class="rule rule--thin"></div>
      </div>
    </header>

    <footer class="footer">
      <div class="footer-contact">
        <address class="footer-address" style="font-style: italic;">
          PO BOX 2841, HARBOUR GATE, QLD 4603, 7 Banksia Road Coral Bay<br>
          12 Wren Lane, Ashgrove
        </address>
        <div class="footer-phones">
          PHONE: 1300 482 615<br>
          MOB: 0412 907 264
        </div>
      </div>
      <div class="rule rule--thick"></div>
      <div class="rule rule--thin"></div>
    </footer>
  </main>
</body>
</html>
```